Geschäftspapiere für Verkauf und Reparatur von Nähmaschinen, Stickmaschinen, etc.
Zielgruppe
Verkauf und Reparatur von Nähmaschinen, Stickmaschinen, etc.
Zielgruppe sind meist Frauen welche das Nähen beruflich ausüben oder es als Hobby betreiben
Aufgabenstellung
Wir wünschen uns eine neue Briefvorlage, welche sich mit unserem Online-Shop widerspiegelt. Alle voran soll das Layout modern sein und unser Logo in den Vordergrund bringen. Elemente aus dem Online-Shop welche unseren Familienbetrieb zeigt dürfen auf gerne enthalten sein.

```html
<!DOCTYPE html>
<html lang="de">
<head>
<meta charset="utf-8">
<title>Briefbogen – Nähwerk Atelier</title>
<link rel="stylesheet" href="https://fonts.googleapis.com/css2?family=Arimo:wght@400;700&family=Open+Sans:wght@400;600&family=Homemade+Apple&display=swap">
<style>
  :root {
    --bg: #e9e9ea;
    --paper: #ffffff;
    --dark: #2a2a2a;
    --red: #e31b23;
    --red-light: #ef4a3b;
    --text: #4a4a4a;
    --ink: #1b2a8c;
    --line: #3a3a3a;
  }
  * { box-sizing: border-box; margin: 0; padding: 0; }
  html, body { width: 1200px; height: 1010px; overflow: hidden; background: var(--bg); }
  .letterhead {
    position: absolute; left: 260px; top: 25px;
    width: 680px; height: 960px;
    background: var(--paper);
    box-shadow: 0 6px 24px rgba(0,0,0,.14);
    overflow: hidden;
    font-family: "Arimo", Arial, sans-serif;
    color: var(--text);
  }
  .header-bands { position: absolute; left: 0; top: 0; }
  .brand {
    position: absolute; left: 34px; top: 24px;
    display: flex; align-items: center; gap: 10px;
    font-family: "Arimo", Arial, sans-serif; font-weight: 700;
    font-size: 26px; letter-spacing: 1px; color: #fff;
  }
  .brand-square { width: 16px; height: 16px; background: var(--red); }
  .contact {
    position: absolute; left: 480px; top: 104px;
    padding-left: 14px; border-left: 1px solid var(--line);
    font-family: "Open Sans", Arial, sans-serif; font-style: normal;
    font-size: 9.5px; line-height: 1.45; color: var(--dark);
  }
  .contact-list { list-style: none; margin-top: 6px; }
  .contact-list li { display: flex; align-items: center; gap: 6px; }
  .contact-list svg { flex: none; }
  .sender-line {
    position: absolute; left: 70px; top: 200px;
    font-family: "Open Sans", Arial, sans-serif; font-size: 8px; color: var(--dark);
    border-bottom: 1px solid var(--dark); padding-bottom: 1px;
  }
  .sender-line .sep { color: var(--red); padding: 0 3px; }
  .fold-mark { position: absolute; left: 0; width: 18px; height: 1px; background: #9a9a9a; }
  .machine-photo {
    position: absolute; left: 300px; top: 420px; width: 380px; height: 440px;
    background: radial-gradient(ellipse at 55% 40%, #f1f1f2 0%, #f6f6f7 55%, rgba(255,255,255,0) 80%);
  }
  .letter-body {
    position: absolute; left: 70px; top: 290px; width: 540px;
    font-size: 13px; line-height: 1.42; color: var(--text);
  }
  .salutation { margin-bottom: 18px; }
  .letter-body p { margin-bottom: 16px; }
  .closing { margin-top: 18px; }
  .letter-body .signature {
    font-family: "Homemade Apple", cursive; color: var(--ink);
    font-size: 26px; margin: 4px 0 6px 10px; line-height: 1.4;
  }
  .signer { font-size: 14px; }
  .footer-info {
    position: absolute; left: 70px; right: 40px; top: 850px;
    display: flex; font-family: "Open Sans", Arial, sans-serif; font-size: 10px; line-height: 1.5; color: var(--dark);
  }
  .footer-col { flex: 1; padding-left: 12px; border-left: 1px solid var(--line); }
  .footer-col:first-child { border-left: none; padding-left: 0; }
  .footer-bands { position: absolute; left: 0; bottom: 0; }
</style>
</head>
<body>
<main class="letterhead">
  <svg class="header-bands" width="680" height="100" viewBox="0 0 680 100" aria-hidden="true">
    <rect x="0" y="0" width="460" height="82" fill="var(--dark)"/>
    <polygon points="430,0 680,0 680,34 470,34 470,80 430,88" fill="var(--red)"/>
    <polygon points="430,52 470,34 470,80 430,88" fill="var(--red-light)"/>
  </svg>
  <div class="brand"><span>NÄHWERK ATELIER</span><span class="brand-square"></span></div>

  <address class="contact">
    Kessler GmbH &amp; Co. KG<br>
    Lindenallee 14<br>
    20817 Beispielstadt
    <ul class="contact-list">
      <li><svg width="9" height="9" viewBox="0 0 10 10"><circle cx="5" cy="5" r="5" fill="var(--red)"/><path d="M3 2.5l1 1-0.6 0.8c.4.9 1 1.5 1.9 1.9l.8-.6 1 1-.8.9C4.8 7.4 2.6 5.2 2.5 3.3z" fill="#fff"/></svg>+49 (0) 3312 - 4810</li>
      <li><svg width="9" height="9" viewBox="0 0 10 10"><circle cx="5" cy="5" r="5" fill="var(--red)"/><rect x="2.6" y="3.5" width="4.8" height="3.2" fill="#fff"/></svg>+49 (0) 3312 - 4819</li>
      <li><svg width="9" height="9" viewBox="0 0 10 10"><circle cx="5" cy="5" r="5" fill="var(--red)"/><rect x="2.5" y="3.2" width="5" height="3.6" fill="#fff"/><path d="M2.5 3.2L5 5.2 7.5 3.2" stroke="var(--red)" stroke-width=".6" fill="none"/></svg>info@naehwerk-atelier.de</li>
      <li><svg width="9" height="9" viewBox="0 0 10 10"><circle cx="5" cy="5" r="5" fill="var(--red)"/><circle cx="5" cy="5" r="2.4" fill="none" stroke="#fff" stroke-width=".8"/></svg>www.naehwerk-atelier.de</li>
    </ul>
  </address>

  <div class="sender-line">Kessler GmbH &amp; Co. KG<span class="sep">|</span>Lindenallee 14<span class="sep">|</span>20817 Beispielstadt</div>

  <span class="fold-mark" style="top:340px"></span>
  <span class="fold-mark" style="top:480px"></span>
  <span class="fold-mark" style="top:680px"></span>

  <div class="machine-photo" role="img" aria-label="Blasses Foto einer Nähmaschine als Hintergrundmotiv"></div>

  <section class="letter-body">
    <p class="salutation">Sehr geehrte Damen und Herren,</p>
    <p>In sollicitudin, metus et posuere blandit, erat dui bibendum eros, id vestibulum sem justo vel mauris. Ut tempor dolor ut justo vulputate, eu blandit libero faucibus. In laoreet, massa non ultricies tempor, est enim auctor mi, sit amet venenatis massa augue in justo. Praesent eu tincidunt diam. Maecenas id mi efficitur tellus interdum consectetur vel sed ante. Sed suscipit quis eros a fermentum. Curabitur ornare sit amet leo eu semper. Vestibulum pretium mi eu nisi. gadde.</p>
    <p>Sed nunc est, iaculis vel enim ut, fringilla commodo lorem. Pellentesque facilisis tempus lorem eget porttitor. Morbi accumsan, nulla accumsan mollis maximus, lectus diam venenatis odio, quis bibendum elit ex a arcu. Fusce turpis erat, euismod sit amet dolor eu, hendrerit rhoncus libero. Phasellus convallis, mi vel pharetra sollicitudin, nisi purus maximus est, nec lobortis dolor enim et augue. Vestibulum auctor mi sit amet leo auctor egestas. Pellentesque eget endrerit rhoncus dan.</p>
    <p class="closing">Mit freundlichen Grüßen</p>
    <p class="signature">Lena Brandt</p>
    <p class="signer">Lena Brandt, LL.M.</p>
  </section>

  <footer class="footer-info">
    <div class="footer-col">Bankverbindung:<br>Sparkasse Talgrund</div>
    <div class="footer-col">BIC: TALGDE21XXX<br>IBAN: DE12 3456 7890 1234 5678 00</div>
    <div class="footer-col">Steuernummer: 204/311/00000<br>Umsatzsteuer-ID-Nr.: DE000000000</div>
  </footer>

  <svg class="footer-bands" width="680" height="60" viewBox="0 0 680 60" aria-hidden="true">
    <polygon points="0,34 600,34 610,22 610,60 0,60" fill="var(--red)"/>
    <polygon points="610,6 680,6 680,60 610,60" fill="var(--dark)"/>
  </svg>
</main>
</body>
</html>
```